Red Sea Boat trips in need of Business Card for Private Boat Tours

We need a Business card for a new business set-up in Egypt on the Red Sea for private snorkelling and boat excursions to one of the world's most beautiful reefs. We have wording logo already set-up which matches the boat but we need business cards to be bright and colourful with pictures of boat

Industry/Entity Type

Tourism

Contact Information for Business Card

Two Silver Gulls (font provided) Boat Trips

```html
<!DOCTYPE html>
<html lang="en">
<head>
<meta charset="utf-8">
<title>Two Silver Gulls – Business Card</title>
<link href="https://fonts.googleapis.com/css2?family=Poppins:wght@400;500;700;800&display=swap" rel="stylesheet">
<style>
  :root{
    --page:#2a2a2a;
    --paper:#ffffff;
    --sky:#bdeaf7;
    --sky-soft:#a9dcee;
    --sea-deep:#0f6f86;
    --sea:#2fb3c9;
    --sea-light:#8fd9e4;
    --ink:#111111;
    --navy:#24305e;
  }
  *{box-sizing:border-box;margin:0;padding:0}
  html,body{width:1200px;height:1015px;overflow:hidden}
  body{background:var(--page);font-family:"Poppins",sans-serif;color:var(--ink);
    display:flex;flex-direction:column;align-items:center;gap:35px;padding-top:33px}
  .card{position:relative;width:800px;height:457px;overflow:hidden;
    box-shadow:0 10px 28px rgba(0,0,0,.55)}
  .card svg.art{position:absolute;inset:0;width:100%;height:100%}

  /* front */
  .card--front{background:var(--paper)}
  .brand{position:absolute;left:60px;top:62px;font-weight:800;font-size:62px;
    letter-spacing:.5px;color:var(--ink);line-height:1}

  /* back */
  .card--back{background:var(--sky)}
  .contact{position:absolute;left:440px;top:96px}
  .contact__name{font-weight:700;font-size:30px;letter-spacing:.5px;text-transform:uppercase;line-height:1.1}
  .contact__role{font-weight:400;font-size:20px;margin-top:2px}
  .contact__phone{font-weight:800;font-size:42px;margin-top:38px;letter-spacing:.5px}
  .contact__address{font-size:21px;line-height:1.3;margin-top:30px}
  .contact__web{font-size:21px;margin-top:30px}
</style>
</head>
<body>

<section class="card card--front">
  <svg class="art" viewBox="0 0 800 457" preserveAspectRatio="none">
    <defs>
      <linearGradient id="seaFront" x1="0" y1="0" x2="1" y2="1">
        <stop offset="0" stop-color="#3aa6c4"/>
        <stop offset=".45" stop-color="#52c7cf"/>
        <stop offset="1" stop-color="#137890"/>
      </linearGradient>
    </defs>
    <path role="img" aria-label="Photo collage: a white motorboat with navy canopy moored at the quay, a snorkeller diving over a coral reef in clear turquoise water, and a second boat near a resort shore"
      fill="url(#seaFront)"
      d="M0 457 L0 330 Q60 318 120 300 Q200 272 280 250 Q380 220 470 168 Q560 120 640 92 Q720 66 800 60 L800 457 Z"/>
  </svg>
  <div class="brand">Two Silver Gulls</div>
</section>

<section class="card card--back">
  <svg class="art" viewBox="0 0 800 457" preserveAspectRatio="none">
    <defs>
      <linearGradient id="seaBack" x1="0" y1="0" x2="1" y2="1">
        <stop offset="0" stop-color="#7fb7d4"/>
        <stop offset=".4" stop-color="#2aa9bf"/>
        <stop offset="1" stop-color="#0f6f86"/>
      </linearGradient>
    </defs>
    <g fill="var(--sky-soft)" opacity=".55">
      <circle cx="560" cy="40" r="48"/>
      <circle cx="630" cy="30" r="42"/>
      <circle cx="700" cy="330" r="50"/>
      <circle cx="760" cy="320" r="46"/>
      <circle cx="300" cy="150" r="40"/>
    </g>
    <path fill="#ffffff" d="M420 185 L800 150 L800 230 L420 262 Z"/>
    <path role="img" aria-label="Photo of a white motorboat with a navy canopy and grey seats moored beside a teak deck on turquoise water"
      fill="url(#seaBack)"
      d="M0 140 Q120 60 250 90 Q360 120 390 240 Q410 350 400 457 L0 457 Z"/>
  </svg>
  <div class="contact">
    <div class="contact__name">Marcus Hale</div>
    <div class="contact__role">Managing Director</div>
    <div class="contact__phone">044-987 654 321</div>
    <div class="contact__address">421, Address line here<br>Country Name, 45452</div>
    <div class="contact__web">www.websitename.com</div>
  </div>
</section>

</body>
</html>
```